Consulting firm needs a professional letterhead design

We need a professional letterhead design which is simple but unique. It should carry attributes of the latest designs in the market suitable for professional environmental consultancies.

- The logo is attached for you to USE.
- Our preferred color scheme is that shown in the logo.
- Letterhead text color is your choice to make.
- Logo to the left and text to the right plus slogan/tagline is desirable for this letterhead.

Use any address etc. of your choice in the letterhead.

Target Market(s)

Consulting firms and government agencies

Industry/Entity Type

Environmental Consultant

Colors
acd037
fece3e
85cae6
3277b5

Requirements
Must have
• Logo supplied and color scheme must be used.
Nice to have
• Nexa font is used in the Logo, so it would ne nice to have nexa font in the letterhead too.

```html
<!DOCTYPE html>
<html lang="en">
<head>
<meta charset="utf-8">
<title>Verdanta Letterhead</title>
<link rel="stylesheet" href="https://fonts.googleapis.com/css2?family=Arimo&family=Montserrat:wght@500;600&family=Red+Hat+Display:wght@600&display=swap">
<style>
  :root {
    --navy: #363c5a;
    --navy-deep: #22243a;
    --ink: #2b2e45;
    --pin: #a8aab3;
    --orange: #f7941d;
    --green: #2fb34a;
    --blue: #1a7fb8;
    --leaf: #acd037;
    --paper: #fdfdfd;
    --white: #ffffff;
  }
  * { margin: 0; padding: 0; box-sizing: border-box; }
  html, body { width: 848px; height: 1200px; overflow: hidden; background: var(--paper); }
  .letterhead { position: relative; width: 848px; height: 1200px; background: var(--paper); overflow: hidden; }

  .brand { position: absolute; left: 38px; top: 43px; width: 170px; text-align: center; }
  .brand-mark { display: block; width: 66px; height: 66px; margin: 4px auto 8px; border-radius: 50%; background: var(--leaf); }
  .brand-name { font-family: "Montserrat", sans-serif; font-weight: 600; font-size: 23px; letter-spacing: 3px; color: var(--navy); line-height: 1; }
  .brand-tagline { font-family: "Montserrat", sans-serif; font-weight: 500; font-size: 9px; color: var(--navy); margin-top: 2px; white-space: nowrap; }

  .divider { position: absolute; left: 229px; top: 49px; width: 3px; height: 97px; background: linear-gradient(var(--orange) 0 33%, var(--green) 33% 66%, var(--blue) 66% 100%); }

  .address { position: absolute; left: 252px; top: 82px; display: flex; gap: 7px; align-items: flex-start; }
  .address svg { width: 17px; height: 28px; margin-top: 2px; }
  .address-text { font-family: "Red Hat Display", sans-serif; font-weight: 600; font-size: 13px; line-height: 16px; color: var(--ink); white-space: nowrap; }

  .footer-wave { position: absolute; left: 0; top: 1064px; width: 848px; height: 136px; }

  .contact { position: absolute; left: 604px; top: 1090px; list-style: none; font-family: "Arimo", sans-serif; font-size: 12.5px; color: var(--white); }
  .contact li { display: flex; align-items: center; height: 24.5px; white-space: nowrap; }
  .contact-icon { width: 14px; height: 14px; margin-right: 4px; display: flex; align-items: center; justify-content: center; font-size: 14px; }
  .contact-icon svg { width: 14px; height: 14px; }
</style>
</head>
<body>
<div class="letterhead">
  <header>
    <div class="brand">
      <span class="brand-mark"></span>
      <div class="brand-name">VERDANTA</div>
      <div class="brand-tagline">Turning evidence into sound policy</div>
    </div>
    <div class="divider"></div>
    <div class="address">
      <svg viewBox="0 0 17 28" aria-hidden="true">
        <path d="M8.5 1a7 7 0 0 0-7 7c0 5 7 13 7 13s7-8 7-13a7 7 0 0 0-7-7z" fill="var(--pin)"/>
        <circle cx="8.5" cy="8" r="2.3" fill="var(--white)"/>
        <ellipse cx="8.5" cy="24" rx="7.5" ry="2.6" fill="none" stroke="var(--pin)" stroke-width="1.5"/>
      </svg>
      <p class="address-text">Plot No.118, Lakshmi Vihar,<br>Station Link Road, Nashik.422001</p>
    </div>
  </header>

  <svg class="footer-wave" viewBox="0 0 848 136" aria-hidden="true">
    <path d="M848 0 L614 0 C566 0 552 58 527 100 C508 128 494 119 470 119 L0 119 L0 136 L848 136 Z" fill="var(--navy-deep)"/>
    <path d="M848 0 L624 0 C578 0 563 58 539 100 C520 128 506 119 482 119 L0 119 L0 136 L848 136 Z" fill="var(--navy)"/>
  </svg>

  <ul class="contact">
    <li>
      <span class="contact-icon"><svg viewBox="0 0 24 24"><path d="M6.6 2.5l3 3.6-2 2.3c1.2 3 3.6 5.7 6.6 7.2l2.2-2 3.7 3-2.4 3.4C10 19.5 4 13 3.3 5z" fill="var(--white)"/></svg></span>
      : +91 540 3172 904
    </li>
    <li>
      <span class="contact-icon">@</span>
      : office@verdanta.com
    </li>
    <li>
      <span class="contact-icon"><svg viewBox="0 0 24 24" fill="none" stroke="var(--white)" stroke-width="1.8"><circle cx="12" cy="12" r="10"/><ellipse cx="12" cy="12" rx="4.5" ry="10"/><path d="M2 12h20M4 7h16M4 17h16"/></svg></span>
      : http://www.verdantaadvisory.com
    </li>
  </ul>
</div>
</body>
</html>
```